WEBSITE DESIGN - www.brondellix.com

We need a professional and modern looking website for our business. The current website was only made tentatively and can be viewed (we expect a website MUCH better than this). It needs to be simple and non-cluttered yet look modern and sophisticated. It needs to be very easy to navigate as our tarket market is people over the age of 45. Our logo is attached below and this should be incorporated plus the colours/theme should match this. We don't mind purchasing images online if your design includes these and we like it.

Any other specific questions please enquire as we want to hear them.

Target Market(s)

over 45 age english speaking westerners

Industry/Entity Type

Business

Number of Pages Required

1 page

Requirements
Must have
• -our logo (attached).
• -page tabs as those described (tabs.. but not necessarily each of these pages completed as well although this would be nice).
• -social media logos
• Pages should include: homepage, services, pricing, about us, contact us. There should also be a payments page designed which would link with the other pages but there would be no tab for this.

```html
<!DOCTYPE html>
<html lang="en">
<head>
<meta charset="utf-8">
<title>Brondellix – Instant Technical Support</title>
<link href="https://fonts.googleapis.com/css2?family=Open+Sans:wght@400;600;700;800&family=Raleway:wght@300;400;500;600&family=Oswald:wght@500;600&display=swap" rel="stylesheet">
<style>
:root{
  --gold:#c08a12;
  --gold-dark:#a87609;
  --ink:#1d1d1d;
  --ink-soft:#2a2a2a;
  --text:#444;
  --muted:#7a7a7a;
  --line:#e2e2e2;
  --pale:#ececec;
  --white:#fff;
}
*{box-sizing:border-box;margin:0;padding:0}
html,body{width:1200px;height:5248px;overflow:hidden}
body{font-family:"Open Sans",Arial,sans-serif;color:var(--text);background:var(--white);position:relative}
.abs{position:absolute}
.section{position:absolute;left:0;width:1200px}
.heading{font-family:"Raleway",Arial,sans-serif;font-weight:400;color:var(--ink);letter-spacing:4px;text-align:center;font-size:38px}
.btn{display:inline-block;background:var(--gold);color:#fff;font-size:15px;text-align:center}

/* top bar */
.topbar{top:0;height:35px;background:var(--ink)}
.topbar .welcome{left:52px;top:11px;font-size:11px;color:#ddd;font-weight:600;letter-spacing:.5px}
.social-mini{right:52px;top:9px;display:flex;gap:5px}
.social-mini span{width:17px;height:17px;background:#5a5a5a;border-radius:2px}

/* header */
.header{top:35px;height:123px;background:var(--white)}
.brand{left:52px;top:38px;display:flex;align-items:center;gap:10px;font-size:30px;font-weight:700;color:var(--ink)}
.brand .mark{width:26px;height:26px;background:var(--gold)}
.nav{left:395px;top:44px;display:flex;align-items:center;gap:12px;font-size:13px;font-weight:700;color:var(--ink)}
.nav a{padding:9px 11px;color:inherit;text-decoration:none}
.nav .current{border:2px solid var(--gold);color:var(--gold)}
.nav .login{background:var(--gold);color:#fff;padding:10px 30px;margin-left:40px}
.nav .contact{background:var(--ink);color:#fff;padding:10px 20px}

/* hero */
.hero{top:158px;height:542px;background:linear-gradient(90deg,#2b2d2e 0%,#3d4144 45%,#55595b 70%,#3c3f41 100%)}
.hero-photo{right:0;top:0;width:620px;height:542px;background:radial-gradient(ellipse at 55% 60%,#7d8b98 0%,#4a5055 55%,rgba(60,63,65,0) 80%)}
.hero h1{left:60px;top:320px;font-family:"Raleway",Arial,sans-serif;font-weight:400;font-size:58px;color:var(--gold);letter-spacing:3px}
.hero p{left:60px;top:395px;font-size:21px;color:#fff}
.hero .btn{left:60px;top:447px;padding:13px 26px}
.dots{display:flex;gap:7px}
.dots span{width:9px;height:9px;border-radius:50%;background:#fff}
.dots .on{background:var(--gold)}
.hero .dots{left:574px;top:496px}

/* services */
.services{top:700px;height:543px;border-bottom:1px solid var(--line)}
.services .heading{position:absolute;top:46px;width:100%}
.service{position:absolute;top:180px;width:260px;text-align:center}
.service .icon{margin:0 auto;width:104px;height:104px;border-radius:50%;background:#fff;box-shadow:0 3px 14px rgba(0,0,0,.15);display:flex;align-items:center;justify-content:center}
.service .icon.featured{width:150px;height:150px;margin-top:-23px;background:var(--gold);box-shadow:none;border:5px solid #fff;outline:1px solid var(--line)}
.service h3{font-size:15px;font-weight:700;color:var(--ink);margin-top:54px}
.service .icon.featured + h3{margin-top:31px}
.service p{font-size:12.5px;color:var(--muted);line-height:20px;margin:12px auto 0;width:220px}

/* priority */
.priority{top:1260px;height:497px;background:var(--pale)}
.priority-photo{left:605px;top:0;width:595px;height:497px;background:linear-gradient(135deg,#d6d4d0 0%,#b9b3ab 45%,#6f6a66 100%)}
.priority h2{left:60px;top:110px;font-family:"Raleway",Arial,sans-serif;font-weight:400;font-size:29px;line-height:36px;color:var(--ink);letter-spacing:1.5px}
.priority p{left:60px;top:200px;width:510px;font-size:13px;line-height:19px;color:#555}
.priority .btn{left:60px;top:350px;padding:11px 30px}

/* why */
.why{top:1785px;height:525px}
.why .heading{position:absolute;top:52px;width:100%}
.why .lead{position:absolute;top:128px;width:100%;text-align:center;font-size:14px;color:#333}
.why .lead b{display:block;color:var(--gold);font-weight:400;margin-top:3px}
.feature{position:absolute;width:420px;display:flex;gap:22px;align-items:flex-start}
.feature h4{font-size:14px;font-weight:700;color:var(--ink);margin-bottom:6px}
.feature p{font-size:13px;line-height:19px;color:#444}
.feature .icon{flex:none;width:74px;height:74px;border-radius:50%;display:flex;align-items:center;justify-content:center}
.feature.left{text-align:right;flex-direction:row-reverse}
.feature.left .icon{background:var(--gold)}
.feature.right .icon{background:#fff;box-shadow:0 2px 10px rgba(0,0,0,.15)}

/* stats */
.stats{top:2328px;height:360px;background:linear-gradient(135deg,#c4900f 0%,#b9850c 50%,#c99516 100%)}
.stat-row{left:60px;top:120px;width:1080px;display:flex;align-items:flex-start;justify-content:space-between;color:#fff}
.stat{text-align:center;width:120px}
.stat .num{font-family:"Raleway",Arial,sans-serif;font-size:36px;margin-top:10px}
.stat .label{font-size:15px;font-weight:700;margin-top:14px;letter-spacing:.5px}
.op{font-size:30px;margin-top:62px}

/* pricing */
.pricing{top:2748px;height:870px}
.pricing .heading{position:absolute;top:38px;width:100%}
.plan{position:absolute;top:132px;width:301px;height:683px;border:1px solid var(--line);text-align:center;background:#fff}
.plan .name{font-size:13px;font-weight:700;color:var(--ink);margin-top:68px;text-align:left;padding-left:18px;letter-spacing:.5px}
.plan .bar{margin-top:12px;height:150px;background:var(--ink);color:#fff;padding-top:12px}
.plan.best .bar{background:var(--gold)}
.plan .term{font-family:"Oswald",Arial,sans-serif;font-size:30px;font-weight:600;letter-spacing:1px}
.price{display:grid;grid-template-columns:60px auto;gap:0 10px;width:130px;margin:6px auto 0;text-align:left;align-items:center}
.price .cur{font-size:13px;text-align:right}
.price .amt{font-family:"Oswald",Arial,sans-serif;font-size:30px;line-height:32px}
.price .amt.sm{font-size:22px;line-height:26px}
.plan .terms{font-size:12.5px;line-height:18px;color:#555;padding:22px 28px 0}
.plan .perks{font-size:17px;font-weight:700;color:var(--ink);line-height:31px;margin-top:22px}
.plan .agree{font-size:11px;color:#555;margin-top:14px;display:flex;align-items:center;justify-content:center;gap:6px}
.plan .agree i{width:11px;height:11px;border:1px solid #777;border-radius:2px}
.plan .order{font-size:26px;font-weight:800;color:var(--gold);margin-top:20px}
.best-tag{position:absolute;left:546px;top:110px;background:var(--gold);color:#fff;font-size:10px;font-weight:700;padding:5px 12px;letter-spacing:.5px}

/* testimonials */
.testimonials{top:3640px;height:438px;background:#f1f1f1}
.testimonials .heading{position:absolute;top:80px;width:100%}
.avatar{left:566px;top:162px;width:68px;height:68px;border-radius:50%;background:linear-gradient(180deg,#d9cfc4,#8f8378);border:3px solid #fff}
.quote{left:220px;top:285px;width:760px;text-align:center;font-size:14px;line-height:21px;color:#333}
.cite{top:352px;width:100%;text-align:center;font-size:12px;font-weight:700;color:var(--gold);letter-spacing:1px}
.cite-url{top:381px;width:100%;text-align:center;font-size:12px;color:#777}
.testimonials .dots{left:565px;top:412px}
.testimonials .dots span{background:#ccc;width:8px;height:8px}
.testimonials .dots .on{background:#666}

/* payments */
.payments{top:4148px;height:175px;display:flex;align-items:center;justify-content:space-between;padding:0 77px}
.card{width:170px;height:78px;display:flex;align-items:center;justify-content:center;font-size:20px;font-weight:700;color:#fff;background:var(--ink-soft)}
.card.light{background:#fff;border:1px solid var(--line);color:var(--ink)}
.badge{width:170px;height:78px;background:#d4d4d4;border-radius:6px}

/* footer */
.footer{top:4358px;height:560px;background:var(--ink)}
.footer h3{font-size:22px;font-weight:700;color:#fff;letter-spacing:.5px}
.about{left:112px;top:40px;width:420px}
.about p{font-size:12.5px;line-height:19px;color:#8a8a8a;margin-top:22px}
.about .btn{margin-top:22px;padding:12px 30px;font-size:13px;font-weight:700}
.contact-item{position:relative;display:flex;gap:28px;border-bottom:1px solid #333;padding:18px 0}
.contact-item .ic{width:20px;flex:none;padding-top:2px}
.contact-item h5{font-size:11px;font-weight:700;color:#fff;letter-spacing:.5px}
.contact-item p{margin-top:6px;font-size:11px;line-height:17px}
.social{display:flex;gap:7px;margin-top:22px}
.social span{width:22px;height:22px;background:var(--gold)}
.drop{left:707px;top:40px;width:380px}
.drop .sub{font-size:11px;color:var(--gold);margin-top:8px}
.field{height:46px;border-bottom:1px solid #333;font-size:11px;color:#777;padding-top:22px}
.field.msg{height:108px}
.drop .btn{margin-top:112px;padding:12px 28px;font-size:12px;font-weight:700}

.map{top:4918px;height:297px;background:linear-gradient(160deg,#dfe4e6 0%,#cfd8dc 50%,#e4e6e2 100%)}
.copyright{top:5215px;height:33px;background:var(--ink);color:#bbb;font-size:12px;text-align:center;line-height:33px}
</style>
</head>
<body>

<div class="section topbar">
  <span class="abs welcome">WELCOME VISITOR</span>
  <div class="abs social-mini"><span></span><span></span><span></span><span></span><span></span></div>
</div>

<header class="section header">
  <div class="abs brand"><span class="mark"></span>Brondellix</div>
  <nav class="abs nav">
    <a class="current">HOME</a><a>FEATURES</a><a>PRICING</a><a>ABOUT US</a><a>CONTACT US</a>
    <a class="login">LOGIN</a><a class="contact">CONTACT US</a>
  </nav>
</header>

<section class="section hero">
  <div class="abs hero-photo" role="img" aria-label="Smiling support technician with arms crossed against a dark chalkboard wall"></div>
  <h1 class="abs">INSTANT SUPPORT</h1>
  <p class="abs">instant technical supports for your devices</p>
  <span class="abs btn">Learn more</span>
  <div class="abs dots"><span class="on"></span><span></span><span></span><span></span></div>
</section>

<section class="section services">
  <h2 class="heading">OUR SERVICES</h2>
  <div class="service" style="left:40px">
    <div class="icon"><svg width="40" height="40" viewBox="0 0 40 40" fill="none" stroke="#c08a12" stroke-width="3"><path d="M8 22a12 12 0 0 1 24 0"/><rect x="5" y="21" width="6" height="10" fill="#c08a12"/><rect x="29" y="21" width="6" height="10" fill="#c08a12"/><path d="M32 31q0 5-8 5"/></svg></div>
    <h3>TECH SUPPORT</h3>
    <p>Consectetuer adipiscing elit, sed diam nonummy nibh euismod tincidunt ut laoreet dolore magna aliquam erat.</p>
  </div>
  <div class="service" style="left:320px">
    <div class="icon"><svg width="44" height="40" viewBox="0 0 44 40"><path d="M11 31a9 9 0 0 1 1-18 12 12 0 0 1 22 4 7 7 0 0 1-1 14z" fill="#555"/><path d="M22 14v12M16 21l6 6 6-6" stroke="#fff" stroke-width="3" fill="none"/></svg></div>
    <h3>DOWNLOADS</h3>
    <p>Consectetuer adipiscing elit, sed diam nonummy nibh euismod tincidunt ut laoreet dolore magna aliquam erat.</p>
  </div>
  <div class="service" style="left:600px">
    <div class="icon featured"><svg width="56" height="50" viewBox="0 0 56 50" fill="none" stroke="#fff" stroke-width="3"><rect x="4" y="6" width="40" height="30"/><path d="M18 44h14M25 36v8M12 28l10-12 8 8 8-10"/></svg></div>
    <h3>WEB DESIGN</h3>
    <p>Consectetuer adipiscing elit, sed diam nonummy nibh euismod tincidunt ut laoreet dolore magna aliquam erat.</p>
  </div>
  <div class="service" style="left:880px">
    <div class="icon"><svg width="40" height="42" viewBox="0 0 40 42" fill="none" stroke="#c08a12" stroke-width="3"><circle cx="20" cy="24" r="14"/><path d="M16 4h8M20 4v6M20 24V16M20 24l6 4"/></svg></div>
    <h3>UNDERSTAND THE URGENCY</h3>
    <p>Consectetuer adipiscing elit, sed diam nonummy nibh euismod tincidunt ut laoreet dolore magna aliquam erat.</p>
  </div>
</section>

<section class="section priority">
  <h2 class="abs">OUR CUSTOMER OUR PRIORITY<br>LETS SAY HI..</h2>
  <p class="abs">Brondellix was established to provide consumers with access to the sophisticated, enterprise-level IT services, support and the benefits and cost savings available to larger organisations, support and the benefits and cost savings available to larger organisations, support and the benefits and cost savings available to larger organisations.<br>We provide proactive monitoring and management of customers entire IT needs.</p>
  <span class="abs btn">Read More</span>
  <div class="abs priority-photo" role="img" aria-label="Bearded man in a checked shirt sipping from a white coffee cup"></div>
</section>

<section class="section why">
  <h2 class="heading">WHY WE ARE THE BEST</h2>
  <p class="lead">The one stop comprehensive diagnostic &amp; repair station for your computer and connected devices.<b>We'll fix anything!</b></p>
  <div class="feature left" style="left:112px;top:250px">
    <div class="icon"><svg width="34" height="34" viewBox="0 0 34 34" stroke="#fff" stroke-width="3.5" fill="none"><path d="M6 28L22 12M20 6a6 6 0 0 0 8 8M28 28L12 12M6 6l5 5"/></svg></div>
    <div><h4>DIAGNOSIS &amp; REPAIR</h4><p>The one stop comprehensive diagnostic &amp; repair station for your computer and connected devices. We'll fix anything!</p></div>
  </div>
  <div class="feature left" style="left:112px;top:380px">
    <div class="icon"><svg width="34" height="34" viewBox="0 0 34 34"><circle cx="17" cy="17" r="11" fill="none" stroke="#fff" stroke-width="6" stroke-dasharray="5 3.6"/><circle cx="17" cy="17" r="5" fill="#fff"/></svg></div>
    <div><h4>OPTIMIZATION</h4><p>The one stop comprehensive diagnostic &amp; repair station for your computer and connected devices. We'll fix anything!</p></div>
  </div>
  <div class="feature right" style="left:628px;top:250px">
    <div class="icon"><svg width="30" height="30" viewBox="0 0 30 30" stroke="#c08a12" stroke-width="3" fill="none"><path d="M15 3v16M9 13l6 6 6-6M4 20v6h22v-6"/></svg></div>
    <div><h4>SETUP &amp; INSTALL</h4><p>The one stop comprehensive diagnostic &amp; repair station for your computer and connected devices. We'll fix anything!</p></div>
  </div>
  <div class="feature right" style="left:628px;top:380px">
    <div class="icon"><svg width="30" height="30" viewBox="0 0 30 30" stroke="#c08a12" stroke-width="3" fill="none"><path d="M8 4v22M15 4v22M22 4v22"/><rect x="5" y="8" width="6" height="5" fill="#c08a12"/><rect x="19" y="16" width="6" height="5" fill="#c08a12"/></svg></div>
    <div><h4>WEB DESIGNING</h4><p>The one stop comprehensive diagnostic &amp; repair station for your computer and connected devices. We'll fix anything!</p></div>
  </div>
</section>

<section class="section stats">
  <div class="abs stat-row">
    <div class="stat"><svg width="44" height="34" viewBox="0 0 44 34" fill="none" stroke="#fff" stroke-width="3"><rect x="8" y="4" width="28" height="20"/><path d="M2 30h40"/></svg><div class="num">986</div><div class="label">LAPTOP</div></div>
    <span class="op">+</span>
    <div class="stat"><svg width="44" height="34" viewBox="0 0 44 34" fill="none" stroke="#fff" stroke-width="3"><rect x="4" y="20" width="36" height="10"/><path d="M14 20V6M30 20V6"/></svg><div class="num">256</div><div class="label">ROUTERS</div></div>
    <span class="op">+</span>
    <div class="stat"><svg width="44" height="34" viewBox="0 0 44 34" fill="none" stroke="#fff" stroke-width="3"><rect x="15" y="2" width="14" height="30" rx="2"/></svg><div class="num">867</div><div class="label">SMART PHONES</div></div>
    <span class="op">+</span>
    <div class="stat"><svg width="44" height="34" viewBox="0 0 44 34" fill="none" stroke="#fff" stroke-width="3"><rect x="4" y="2" width="36" height="22"/><path d="M22 24v6M14 32h16"/></svg><div class="num">1904</div><div class="label">DESKTOPS</div></div>
    <span class="op">+</span>
    <div class="stat"><svg width="44" height="34" viewBox="0 0 44 34" fill="none" stroke="#fff" stroke-width="3"><rect x="11" y="2" width="22" height="30" rx="2"/></svg><div class="num">511</div><div class="label">TABLETS</div></div>
    <span class="op">+</span>
    <div class="stat" style="width:220px"><svg width="44" height="34" viewBox="0 0 44 34" stroke="#fff" stroke-width="4" fill="none"><path d="M10 30L30 8M28 4a6 6 0 0 0 8 8M34 30L14 10M8 4l6 6"/></svg><div class="num">2456</div><div class="label">SOFTWARE INSTALLATION</div></div>
    <span class="op">=</span>
    <div class="stat"><svg width="44" height="34" viewBox="0 0 44 34" fill="none" stroke="#fff" stroke-width="3"><path d="M6 16h24a10 10 0 0 1-10 14H16A10 10 0 0 1 6 16zM30 18h4a4 4 0 0 1 0 8h-5M16 4q4 4 0 8"/></svg><div class="num">26</div><div class="label">EXPERIENCE</div></div>
  </div>
</section>

<section class="section pricing">
  <h2 class="heading">PERFECT PACKAGE FOR YOU</h2>
  <span class="best-tag">BEST SELLER</span>
  <div class="plan" style="left:77px">
    <div class="name">STARTER</div>
    <div class="bar"><div class="term">SIX MONTHS</div>
      <div class="price"><span class="cur">NZD</span><span class="amt">95</span><span class="cur">USD</span><span class="amt sm">60*</span><span class="cur">GBP</span><span class="amt sm">40*</span></div></div>
    <p class="terms">The price advertised might not be the same price charged to the credit card account due to exchange rate fluctuations. This means that because we are based in New Zealand we have to convert your purchase to New Zealand dollars at the exchange rate on the day it is processed.</p>
    <div class="perks">1 Month Tech Support<br>For 1 Computer<br>24X7 Availability</div>
    <div class="agree"><i></i>I agree to the Terms and Conditions</div>
    <div class="order">Order Now!</div>
  </div>
  <div class="plan best" style="left:462px">
    <div class="name">QUICK FIX</div>
    <div class="bar"><div class="term">SIX MONTHS</div>
      <div class="price"><span class="cur">NZD</span><span class="amt">95</span><span class="cur">USD</span><span class="amt sm">60*</span><span class="cur">GBP</span><span class="amt sm">40*</span></div></div>
    <p class="terms">The price advertised might not be the same price charged to the credit card account due to exchange rate fluctuations. This means that because we are based in New Zealand we have to convert your purchase to New Zealand dollars at the exchange rate on the day it is processed.</p>
    <div class="perks">1 Month Tech Support<br>For 1 Computer<br>24X7 Availability</div>
    <div class="agree"><i></i>I agree to the Terms and Conditions</div>
    <div class="order">Order Now!</div>
  </div>
  <div class="plan" style="left:872px">
    <div class="name">ADVANCE</div>
    <div class="bar"><div class="term">SIX MONTHS</div>
      <div class="price"><span class="cur">NZD</span><span class="amt">95</span><span class="cur">USD</span><span class="amt sm">60*</span><span class="cur">GBP</span><span class="amt sm">40*</span></div></div>
    <p class="terms">The price advertised might not be the same price charged to the credit card account due to exchange rate fluctuations. This means that because we are based in New Zealand we have to convert your purchase to New Zealand dollars at the exchange rate on the day it is processed.</p>
    <div class="perks">1 Month Tech Support<br>For 1 Computer<br>24X7 Availability</div>
    <div class="agree"><i></i>I agree to the Terms and Conditions</div>
    <div class="order">Order Now!</div>
  </div>
</section>

<section class="section testimonials">
  <h2 class="heading">WHY CUSTOMERS LOVE US</h2>
  <div class="abs avatar" role="img" aria-label="Portrait photo of the reviewing customer"></div>
  <p class="abs quote">Many desktop publishing packages and web page editors now use Lorem Ipsum as their default model text search for lorem ipsum will uncover many web sites still in their infancy....</p>
  <div class="abs cite">MARLA PENHURST</div>
  <div class="abs cite-url">penhurstlane.com</div>
  <div class="abs dots"><span class="on"></span><span></span><span></span><span></span><span></span></div>
</section>

<section class="section payments">
  <div class="card" style="background:#2d6fa8">Crestpay</div>
  <div class="card light">Norvia</div>
  <div class="card">Tallcard</div>
  <div class="badge"></div>
  <div class="card light">Pennmark</div>
</section>

<footer class="section footer">
  <div class="abs about">
    <h3>ABOUT US</h3>
    <p>Quick service, friendly staff and fair pricing for every home and small office. We handle repairs, setups and support so your devices simply work.</p>
    <span class="btn">READ MORE</span>
    <div class="contact-item" style="margin-top:30px">
      <svg class="ic" viewBox="0 0 20 24" fill="#aaa"><path d="M10 0a8 8 0 0 1 8 8c0 6-8 16-8 16S2 14 2 8a8 8 0 0 1 8-8z"/><circle cx="10" cy="8" r="3" fill="#1d1d1d"/></svg>
      <div><h5>ADDRESS</h5><p>12 Harbour Lane, Kelburn Court,<br>Wellington 6011</p></div>
    </div>
    <div class="contact-item">
      <svg class="ic" viewBox="0 0 20 20" fill="#aaa"><path d="M4 1l4 4-2 3q2 4 6 6l3-2 4 4-3 3Q7 18 1 4z"/></svg>
      <div><h5>PHONE</h5><p>+64 4 555 0182 | Mobile: +64 21 555 047</p></div>
    </div>
    <div class="contact-item">
      <svg class="ic" viewBox="0 0 20 16" fill="none" stroke="#aaa" stroke-width="2"><rect x="1" y="1" width="18" height="14"/><path d="M1 1l9 8 9-8"/></svg>
      <div><h5>EMAIL</h5><p>support@brondellix.com<br>info@brondellix.com</p></div>
    </div>
    <div class="social"><span></span><span></span><span></span><span></span><span></span><span></span><span></span></div>
  </div>
  <div class="abs drop">
    <h3>DROP US A LINE</h3>
    <div class="sub">Mail Us Your Message</div>
    <div class="field">Name</div>
    <div class="field">Email</div>
    <div class="field">Subject</div>
    <div class="field msg">Write Your Message</div>
    <span class="btn">SEND MESSAGE</span>
  </div>
</footer>

<div class="section map" role="img" aria-label="Street map showing the office location"></div>
<div class="section copyright">Copyrights 2016 © brondellix.com</div>

</body>
</html>
```